business card and letter head for Australian company manufacturing rienforcing steel for constructio

business card and letter head using our logo. you will need to change the name of the logo to KOLVATIN and the red part of the logo needs to start at the e after d.

Architects, Engineers, Builders, Developers

Manufacturing

```html
<!DOCTYPE html>
<html lang="en">
<head>
<meta charset="utf-8">
<title>Kolvatin – Business Cards and Letterhead</title>
<link rel="stylesheet" href="https://fonts.googleapis.com/css2?family=Roboto+Condensed:wght@700&display=swap">
<style>
  :root {
    --lime: #76e600;
    --maroon: #930000;
    --charcoal: #2f3131;
    --badge: #3fe6a4;
    --paper: #ffffff;
    --font: "Roboto Condensed", "Arial Narrow", sans-serif;
  }
  * { margin: 0; padding: 0; box-sizing: border-box; }
  html, body { width: 959px; height: 1200px; overflow: hidden; background: var(--paper); }
  body { position: relative; font-family: var(--font); font-weight: 700; color: var(--charcoal); }

  .card { position: absolute; width: 289px; height: 405px; background: var(--lime); overflow: hidden; }
  .card--front-a { left: 171px; top: 3px; }
  .card--back-a  { left: 523px; top: 3px; }
  .card--front-b { left: 175px; top: 485px; }
  .card--back-b  { left: 527px; top: 485px; }
  .card-bands { position: absolute; inset: 0; width: 100%; height: 100%; }
  .band-top { fill: var(--maroon); }
  .band-bottom { fill: var(--charcoal); }

  .brand-dot { position: absolute; left: 50%; transform: translateX(-50%); border-radius: 50%; background: var(--charcoal); }
  .brand-name { position: absolute; left: 0; right: 0; text-align: center; color: var(--maroon); letter-spacing: 1px; line-height: 1; }

  .contact { position: absolute; left: 0; right: 0; text-align: center; list-style: none; font-size: 18px; }
  .web { position: absolute; left: 0; right: 0; text-align: center; font-size: 23px; line-height: 1; }

  .member-badge { position: absolute; width: 24px; height: 17px; border-radius: 9px 4px 9px 4px; background: var(--badge); }

  /* Front A */
  .card--front-a .brand-dot { top: 140px; width: 100px; height: 100px; }
  .card--front-a .brand-name { top: 258px; font-size: 30px; }

  /* Back A */
  .card--back-a .brand-dot { top: 24px; width: 70px; height: 70px; }
  .card--back-a .brand-name { top: 115px; font-size: 30px; }
  .card--back-a .contact { top: 158px; line-height: 23px; }
  .card--back-a .web { top: 326px; }
  .card--back-a .member-badge { left: 189px; top: 380px; }

  /* Front B */
  .card--front-b .brand-dot { top: 112px; width: 120px; height: 120px; }
  .card--front-b .brand-name { top: 264px; font-size: 40px; }

  /* Back B */
  .card--back-b .brand-dot { top: 60px; width: 64px; height: 64px; }
  .card--back-b .brand-name { top: 139px; font-size: 29px; }
  .card--back-b .contact { top: 180px; line-height: 21.7px; }
  .card--back-b .web { top: 336px; }
  .card--back-b .member-badge { left: 189px; top: 381px; }

  /* Letterhead */
  .letterhead { position: absolute; left: 0; top: 933px; width: 959px; height: 267px; background: var(--lime); }
  .letterhead .brand-dot { top: 22px; width: 72px; height: 72px; }
  .letterhead .brand-name { top: 110px; font-size: 34px; }
  .letterhead-contact { position: absolute; left: 0; right: 0; display: flex; justify-content: center; gap: 24px; font-size: 19px; line-height: 1; }
  .letterhead-contact--phones { top: 160px; }
  .letterhead-contact--address { top: 187px; }
  .letterhead .web { top: 212px; font-size: 31px; }
</style>
</head>
<body>

  <section class="card card--front-a" aria-label="Business card front">
    <svg class="card-bands" viewBox="0 0 289 405" preserveAspectRatio="none" aria-hidden="true">
      <path class="band-top" d="M0 0H289V49Q144.5 9 0 49Z"/>
      <path class="band-bottom" d="M0 356Q144.5 396 289 356V405H0Z"/>
    </svg>
    <div class="brand-dot"></div>
    <p class="brand-name">KOLVATIN</p>
  </section>

  <section class="card card--back-a" aria-label="Business card back">
    <svg class="card-bands" viewBox="0 0 289 405" preserveAspectRatio="none" aria-hidden="true">
      <path class="band-bottom" d="M0 356Q144.5 396 289 356V405H0Z"/>
    </svg>
    <div class="brand-dot"></div>
    <p class="brand-name">KOLVATIN</p>
    <ul class="contact">
      <li>Ph 07 5550 1846</li>
      <li>Fax 07 5550 1847</li>
      <li>Mobile 0400 555 319</li>
      <li>hello@kolvatin.com</li>
      <li>14 Ridge Rd Harlow</li>
      <li>Qld 4999 Australia</li>
    </ul>
    <p class="web">www.kolvatin.com</p>
    <div class="member-badge" aria-hidden="true"></div>
  </section>

  <section class="card card--front-b" aria-label="Business card front, alternative">
    <svg class="card-bands" viewBox="0 0 289 405" preserveAspectRatio="none" aria-hidden="true">
      <path class="band-top" d="M0 0H289V49Q144.5 9 0 49Z"/>
      <path class="band-bottom" d="M0 356Q144.5 396 289 356V405H0Z"/>
    </svg>
    <div class="brand-dot"></div>
    <p class="brand-name">KOLVATIN</p>
  </section>

  <section class="card card--back-b" aria-label="Business card back, alternative">
    <svg class="card-bands" viewBox="0 0 289 405" preserveAspectRatio="none" aria-hidden="true">
      <path class="band-top" d="M0 0H289V49Q144.5 9 0 49Z"/>
      <path class="band-bottom" d="M0 356Q144.5 396 289 356V405H0Z"/>
    </svg>
    <div class="brand-dot"></div>
    <p class="brand-name">KOLVATIN</p>
    <ul class="contact">
      <li>Ph 07 5550 1846</li>
      <li>Fax 07 5550 1847</li>
      <li>Mobile 0400 555 319</li>
      <li>hello@kolvatin.com</li>
      <li>14 Ridge Rd Harlow</li>
      <li>Qld 4999 Australia</li>
    </ul>
    <p class="web">www.kolvatin.com</p>
    <div class="member-badge" aria-hidden="true"></div>
  </section>

  <section class="letterhead" aria-label="Letterhead">
    <div class="brand-dot"></div>
    <p class="brand-name">KOLVATIN</p>
    <p class="letterhead-contact letterhead-contact--phones">
      <span>Ph 07 5550 1846</span>
      <span>Fax 07 5550 1847</span>
      <span>Mobile 0400 555 319</span>
    </p>
    <p class="letterhead-contact letterhead-contact--address">
      <span>hello@kolvatin.com</span>
      <span>14 Ridge Rd Harlow</span>
      <span>Qld 4999 Australia</span>
    </p>
    <p class="web">www.kolvatin.com</p>
  </section>

</body>
</html>
```